Landing Page IT Security Vendor

We need a landing page that uses our colour scheme (www.veldonguard.com). We created a draft (see attached). We do not need standard stock template design pages. Please only apply if you can design pages from scratch and try to be as close as possible to our draft. It is ok to also purchase commecrial stock pictures

Coding

Coded - Design and coding required

Number of Pages Required

1 page

```html
<!DOCTYPE html>
<html lang="en">
<head>
<meta charset="utf-8">
<title>Veldon Guard – Security Awareness Training</title>
<link href="https://fonts.googleapis.com/css2?family=Poppins:wght@300;400;500;600;700&display=swap" rel="stylesheet">
<style>
:root{
  --teal:#00b3bd;
  --teal-dark:#0a8f97;
  --sky:#a9dfe9;
  --orange:#f9a61a;
  --ink:#222;
  --muted:#555;
  --night:#1d1f22;
  --white:#fff;
}
*{box-sizing:border-box;margin:0;padding:0}
html,body{width:1200px;height:2837px;overflow:hidden}
body{font-family:"Poppins",sans-serif;color:var(--ink);background:var(--white)}
.page{position:relative;width:1200px;height:2837px;overflow:hidden}
.abs{position:absolute}

/* header */
.site-header{left:0;top:0;width:1200px;height:102px;background:var(--white);border-top:2px solid var(--teal)}
.brand{left:68px;top:22px;display:flex;align-items:center;gap:8px;font-weight:700;font-size:34px;color:var(--ink)}
.brand-dot{width:44px;height:44px;border-radius:50%;background:var(--orange)}
.main-nav{right:70px;top:31px;display:flex;align-items:center;gap:34px;font-size:20px;color:#333}
.main-nav .active{background:var(--teal);color:var(--white);padding:6px 16px;border-radius:22px}
.caret{font-size:12px;margin-left:3px}

/* hero */
.hero{left:0;top:102px;width:1200px;height:599px;background:linear-gradient(90deg,#1fb7c6 0%,#3cc0cc 45%,#3a7da3 75%,#22466b 100%)}
.hero-photo{right:0;top:0;width:560px;height:599px;background:radial-gradient(circle at 40% 45%,rgba(170,230,240,.5),rgba(40,80,120,0) 60%)}
.award-bar{left:70px;top:0;width:1060px;height:60px;background:var(--night);display:flex;align-items:center;color:var(--white);font-size:11.5px;line-height:17px}
.award{flex:1;display:flex;align-items:center;gap:14px;padding-left:18px}
.award b{font-weight:600}
.hero-kicker{left:69px;top:176px;font-size:33px;font-weight:600;color:var(--white)}
.hero-title{left:69px;top:236px;font-size:46px;font-weight:300;line-height:48px;letter-spacing:2px;color:var(--white)}
.btn-ghost{left:70px;top:417px;width:230px;height:59px;border:2px solid var(--white);border-radius:30px;background:rgba(255,255,255,.35);color:#3a8f9a;font-size:20px;display:flex;align-items:center;justify-content:center;letter-spacing:.5px}

/* help section */
.help{left:0;top:701px;width:1200px;height:678px;background:var(--sky)}
.section-title{left:0;top:50px;width:1200px;text-align:center;font-size:30px;font-weight:600;letter-spacing:2px}
.title-rule{left:565px;top:96px;width:70px;height:3px;background:var(--ink)}
.card{top:150px;width:341px;height:439px;background:var(--white);border:1px solid #cfe8ee;text-align:center}
.card-head{height:98px;display:flex;flex-direction:column;justify-content:center;color:var(--teal-dark);font-size:19px;font-weight:500;letter-spacing:.8px;line-height:24px;padding:0 8px}
.card-head small{font-size:14px;letter-spacing:.6px}
.card-band{height:137px;background:var(--teal-dark);color:var(--white);font-size:16.5px;font-weight:700;line-height:20px;display:flex;align-items:center;justify-content:center;padding:0 40px}
.card-body{padding:26px 24px 0;font-size:16px;line-height:20px;color:#333}
.btn-orange{background:var(--orange);color:var(--white);border-radius:30px;display:flex;align-items:center;justify-content:center;font-size:16px;letter-spacing:.5px}
.card .btn-orange{position:absolute;left:50px;top:409px;width:240px;height:58px}

/* mssp band */
.mssp{left:0;top:1379px;width:1200px;height:150px;background:linear-gradient(90deg,#1a1c1f 0%,#23343d 50%,#2f6a7b 80%,#1d3c4a 100%)}
.mssp-text{left:148px;top:28px;font-size:30px;color:var(--white);font-weight:400}
.btn-teal{left:150px;top:75px;width:160px;height:39px;background:var(--teal);color:var(--white);border-radius:20px;font-size:16px;display:flex;align-items:center;justify-content:center}

/* trust */
.trust{left:0;top:1529px;width:1200px;text-align:center}
.trust h2{margin-top:52px;font-size:43px;font-weight:400;line-height:48px;letter-spacing:1.5px}
.trust h2 em{font-style:normal;color:var(--orange);font-weight:500}
.trust h2 strong{font-weight:700}
.trust p{font-size:26px;line-height:36px;font-weight:300;color:#333}
.trust .lead{margin-top:18px}
.trust .strong{font-weight:500;margin-top:22px}
.trust .more{margin-top:20px}
.trust .more b{font-weight:600}
.cta{left:300px;top:1962px;width:600px;height:69px;font-size:20px;font-weight:500}
.rule{left:70px;top:2072px;width:1060px;height:1px;background:#ccc}
.clients{left:70px;top:2120px;width:1060px;height:102px;display:flex;align-items:center;justify-content:space-between}
.client{width:150px;height:100px;display:flex;align-items:center;justify-content:center;font-size:24px;font-weight:600;color:var(--muted)}

/* footer */
.site-footer{left:0;top:2272px;width:1200px;height:565px;background:var(--teal);color:var(--white)}
.f-label{font-size:15px;font-weight:600;letter-spacing:1px}
.f-text{font-size:15px;line-height:26px;letter-spacing:.5px}
.pin{width:44px;height:44px;border-radius:8px;background:var(--night);display:flex;align-items:center;justify-content:center}
.f-head{display:flex;align-items:center;gap:20px}
.social{display:flex;gap:10px}
.social span{width:30px;height:30px;border-radius:50%;background:var(--white)}
.social span:first-child{background:var(--night)}
.f-rule{left:70px;top:425px;width:1060px;height:1px;background:rgba(255,255,255,.7)}
.f-brand{left:69px;top:462px;display:flex;align-items:center;gap:8px;font-size:34px;font-weight:700;color:var(--night)}
.copyright{left:69px;top:532px;font-size:13px}
.badges{left:330px;top:462px;width:800px;display:flex;justify-content:space-between;align-items:center}
.badge{width:58px;height:62px;background:rgba(255,255,255,.85)}
.badge.round{border-radius:50%}
.badge.dark{background:#26324a}
.badge.red{background:#c8202e}
</style>
</head>
<body>
<div class="page">

  <header class="site-header abs">
    <div class="brand abs"><span class="brand-dot"></span>Veldon</div>
    <nav class="main-nav abs">
      <span class="active">Home</span>
      <span>Solution<span class="caret">▾</span></span>
      <span>Pricing</span>
      <span>Resources<span class="caret">▾</span></span>
      <span>About<span class="caret">▾</span></span>
    </nav>
  </header>

  <section class="hero abs">
    <div class="hero-photo abs" role="img" aria-label="Business person holding a tablet with financial data overlays"></div>
    <div class="award-bar abs">
      <div class="award">
        <svg width="30" height="30" viewBox="0 0 30 30" fill="none" stroke="#fff" stroke-width="2"><path d="M8 4h14v8a7 7 0 0 1-14 0z"/><path d="M8 7H3c0 5 3 7 5 7M22 7h5c0 5-3 7-5 7M15 19v5M10 26h10"/></svg>
        <span>In 2020 VELDON won the Digital Defense<br>Excellence Award for Best <b>"Anti Phishing"</b></span>
      </div>
      <div class="award">
        <svg width="30" height="30" viewBox="0 0 30 30" fill="none" stroke="#fff" stroke-width="2"><circle cx="15" cy="18" r="8"/><circle cx="15" cy="18" r="3"/><path d="M6 3l9 7 9-7"/></svg>
        <span>In 2020 VELDON won the Digital Defense Excellence<br>Award for Best <b>"Security Education Platform"</b></span>
      </div>
      <div class="award">
        <svg width="30" height="30" viewBox="0 0 30 30" fill="none" stroke="#fff" stroke-width="2"><path d="M9 4h12v7a6 6 0 0 1-12 0z"/><path d="M15 17v6M10 26h10M4 6l3 3M26 6l-3 3"/></svg>
        <span>2020 Gold Winner <b>"Security Education Platform"</b><br>and Training <b>"in the Security Products Review"</b></span>
      </div>
    </div>
    <h1 class="hero-kicker abs">CYBER SECURITY STARTS WITH PEOPLE</h1>
    <p class="hero-title abs">TRAIN YOUR STAFF WITH<br>VELDON AND IMPROVE CYBER<br>SECURITY AWARENESS</p>
    <a class="btn-ghost abs">Request a demo</a>
  </section>

  <section class="help abs">
    <h2 class="section-title abs">HOW CAN WE HELP</h2>
    <div class="title-rule abs"></div>

    <article class="card abs" style="left:70px">
      <div class="card-head">IMPORT OUR TRAINING<br>COURSES IN YOUR LMS</div>
      <div class="card-band">Buy out the box or custom tailored security courses you can import in your elearning (SCORM)</div>
      <p class="card-body">VELDON offers 250 fully customizable training modules in +30 languages. Games, Videos, Exams, Posters, offline, micro training and much more!</p>
      <a class="btn-orange">EXPLORE OUR TRAINING</a>
    </article>

    <article class="card abs" style="left:429px">
      <div class="card-head">LET US DEVELOP A SECURITY<br>AWARNESS PROGRAM</div>
      <div class="card-band">VELDON Security will assist you in improving security awareness with money back gurantee!</div>
      <p class="card-body">Our security awareness specialists will identify risky users via phishing simulations. we develop a tailored awarness program and reduce your exposure to social hacking.</p>
      <a class="btn-orange">EXPLORE OUR SERVICES</a>
    </article>

    <article class="card abs" style="left:789px">
      <div class="card-head">INSTALL THE VELDON SOFTWARE<br><small>ON PREMISE OR ACCES SAAS VERSION</small></div>
      <div class="card-band">You want to run the campaign yourself?<br>choose your prefered setup type and get started in 24h!</div>
      <p class="card-body">The VELDON software can be installed on premise or in the cloud.<br>If you don't want to deal with installation we onboard you in 24h on our SaaS!</p>
      <a class="btn-orange">EXPLORE OUR SOFTWARE</a>
    </article>
  </section>

  <section class="mssp abs" role="img" aria-label="Dark network and data graphic background">
    <p class="mssp-text abs">VELDON is also Available for <b>MSSP</b></p>
    <a class="btn-teal abs">Learn More</a>
  </section>

  <section class="trust abs">
    <h2>Already over <em>12.000.00</em> Employees worlwide<br>trust and use <strong>VELDON.</strong></h2>
    <p class="lead">VELDON Security is a name you can trust! Because we have won countless<br>awards since 2015 and help Well-known brands around the world.</p>
    <p class="strong">You know You're getting quality solutions with us.</p>
    <p class="more">Our Services can be cusomized to fit your needs and company size.<br><b>Talk to our team today to learn more.</b></p>
  </section>
  <a class="cta btn-orange abs">GET IN CONTACT WITH THE VELDON TEAM NOW</a>
  <div class="rule abs"></div>

  <div class="clients abs">
    <svg width="40" height="60" viewBox="0 0 40 60" fill="none" stroke="#111" stroke-width="2"><path d="M36 4L4 30l32 26"/></svg>
    <div class="client">Norvak</div>
    <div class="client">Railtrek</div>
    <div class="client">Assurio</div>
    <div class="client">Heimwert</div>
    <div class="client">Kornfeld</div>
    <svg width="40" height="60" viewBox="0 0 40 60" fill="none" stroke="#111" stroke-width="2"><path d="M4 4l32 26L4 56"/></svg>
  </div>

  <footer class="site-footer abs">
    <div class="abs f-label" style="left:69px;top:64px">CONTACT DETAILS</div>

    <div class="abs f-head" style="left:69px;top:92px">
      <span class="pin"><svg width="18" height="24" viewBox="0 0 18 24" fill="none" stroke="#fff" stroke-width="1.6"><path d="M9 23s8-9 8-14A8 8 0 0 0 1 9c0 5 8 14 8 14z"/><circle cx="9" cy="9" r="3"/></svg></span>
      <span class="f-label">EUROPE</span>
    </div>
    <p class="abs f-text" style="left:69px;top:152px">VELDON GUARD AG<br>SEESTRASSE 18 | 8800 THALWIL | SWITZERLAND</p>

    <div class="abs f-head" style="left:69px;top:232px">
      <span class="pin"><svg width="18" height="24" viewBox="0 0 18 24" fill="none" stroke="#fff" stroke-width="1.6"><path d="M9 23s8-9 8-14A8 8 0 0 0 1 9c0 5 8 14 8 14z"/><circle cx="9" cy="9" r="3"/></svg></span>
      <span class="f-label">NORTH AMERICA</span>
    </div>
    <p class="abs f-text" style="left:69px;top:292px">VELDON GUARD USA<br>4120 HARBOR LANE<br>SUITE 210<br>DENVER, CO 80202</p>

    <div class="abs f-head" style="left:489px;top:92px">
      <span class="pin"><svg width="18" height="24" viewBox="0 0 18 24" fill="none" stroke="#fff" stroke-width="1.6"><path d="M9 23s8-9 8-14A8 8 0 0 0 1 9c0 5 8 14 8 14z"/><circle cx="9" cy="9" r="3"/></svg></span>
      <span class="f-label">GIVE US A CALL</span>
    </div>
    <p class="abs f-text" style="left:489px;top:152px">PHONE GLOBAL: +41 44 555 01 20<br>PHONE USA: +1-303-555-0148<br>PHONE USA SUPPORT: +1-303-555-0163<br>PHONE FRANCE: +33 6 55 50 12 34<br>PHONE UK: +44 (0) 7700 900412</p>

    <div class="abs f-label" style="left:869px;top:106px">FOLLOW US</div>
    <div class="abs social" style="left:869px;top:150px"><span></span><span></span><span></span><span></span></div>
    <div class="abs f-label" style="left:869px;top:220px">LANGUAGE</div>
    <div class="abs f-text" style="left:869px;top:246px">English ▾</div>

    <div class="f-rule abs"></div>
    <div class="f-brand abs"><span class="brand-dot"></span>Veldon</div>
    <div class="copyright abs">Veldon Guard All Rights Reserved © 2020.</div>
    <div class="badges abs">
      <span class="badge"></span>
      <span class="badge round"></span>
      <span class="badge"></span>
      <span class="badge dark"></span>
      <span class="badge red"></span>
      <span class="badge"></span>
      <span class="badge red"></span>
      <span class="badge dark"></span>
      <span class="badge round"></span>
    </div>
  </footer>

</div>
</body>
</html>
```